Electrician Business needs flyer for discount offer and advertise services

Need a promotional flyer that will grab attention,, offer:

During the months of October & November receive a 10% discount on;
Ceiling fan installation
Smoke alarm installation
Replace existing downlights for new LED downlights.
Offer expires 30th November 2016
'Keep cool, stay safe and save power with VoltMate'

Would like to advertise services and quality on reverse-side. Can have graphic pointing to reverse side on both sides, encouraging customer to read both sides of flyer.
Contact details both sides
Design to suit two-sided A5

Reverse side list services;

All residential & commercial electrical services
Electrical contracting
Real estate/strata electrical maintenance & repairs
New builds
Renovations
Security sensor lighting
Ceiling fans
Smoke Alarms
Data connections

Target Market(s)

Residential home owners and commercial, building and construction companies

Industry/Entity Type

Electrical

Font styles to use
Serif

Colors
0255a3
ffffff

Requirements
Nice to have
• A picture of a modern ceiling fan.
• Arrow/graphic pointing to reverse side, so customer reads both sides of flyer

```html
<!DOCTYPE html>
<html lang="en">
<head>
<meta charset="utf-8">
<title>VoltMate Electrical Services – Two-sided A5 Flyer</title>
<link rel="stylesheet" href="https://fonts.googleapis.com/css2?family=Roboto+Condensed:ital,wght@0,400;0,700;1,400;1,700&family=Oswald:wght@600;700&display=swap">
<style>
  :root{
    --brand-blue:#0255a3;
    --bright-blue:#1a8ff0;
    --sky-blue:#3fa9f0;
    --deep-indigo:#2a2f96;
    --indigo-light:#3b55c8;
    --white:#ffffff;
    --yellow:#ffe100;
    --gold:#ffd200;
    --orange:#ff8a00;
    --stage:#123a62;
    --shadow:rgba(0,20,60,.55);
  }
  *{box-sizing:border-box;margin:0;padding:0}
  html,body{width:1200px;height:1200px;overflow:hidden}
  body{background:var(--stage);font-family:"Roboto Condensed",sans-serif;position:relative}

  .flyer{position:absolute;top:218px;width:540px;height:764px;overflow:hidden}
  .flyer--front{left:40px;background:linear-gradient(160deg,#0c6bd0 0%,var(--bright-blue) 40%,#0a63c6 70%,var(--brand-blue) 100%)}
  .flyer--back{left:620px;background:radial-gradient(ellipse at 30% 25%,var(--indigo-light) 0%,var(--deep-indigo) 55%,#23287f 100%)}

  .decor{position:absolute;inset:0;width:100%;height:100%}

  .fan-photo{position:absolute;left:0;top:20px;width:420px;height:320px;
    background:radial-gradient(ellipse at 40% 55%,rgba(240,248,255,.95) 0%,rgba(170,215,250,.75) 28%,rgba(80,160,235,.35) 55%,transparent 78%)}

  .corner-arrow{position:absolute;left:0;top:0;width:130px;height:110px}

  .brand{position:absolute;right:32px;text-align:right;color:var(--white)}
  .brand__name{display:block;font-weight:700;font-size:50px;line-height:1;letter-spacing:.5px;color:var(--white)}
  .brand__sub{display:block;font-weight:700;font-size:18px;line-height:1.2;margin-top:2px}

  .tagline{position:absolute;right:40px;top:158px;text-align:right;color:var(--white);
    font-style:italic;font-weight:700;font-size:17px;line-height:1.4;text-shadow:0 1px 3px var(--shadow)}

  .offer-intro{position:absolute;right:36px;top:258px;text-align:right;color:var(--white);font-weight:700;text-shadow:0 2px 4px var(--shadow)}
  .offer-intro__line{display:block;font-size:25px;line-height:1.25}
  .offer-intro__months{display:block;font-size:36px;line-height:1.05;color:var(--yellow)}
  .offer-intro__pct{color:var(--yellow)}

  .deal-list{position:absolute;right:36px;top:382px;list-style:none;text-align:right;white-space:nowrap}
  .deal-list li{font-weight:700;font-size:33px;line-height:57px;color:var(--orange);
    text-shadow:-1.5px -1.5px 0 var(--white),1.5px -1.5px 0 var(--white),-1.5px 1.5px 0 var(--white),1.5px 1.5px 0 var(--white),0 3px 6px var(--shadow)}
  .deal-list .bolt{width:22px;height:30px;vertical-align:-3px;margin-right:4px}

  .expiry{position:absolute;right:40px;top:636px;color:var(--white);font-style:italic;font-size:13px}

  .call-bar{position:absolute;right:0;height:80px;color:var(--yellow);display:flex;align-items:center;white-space:nowrap}
  .call-bar__band{position:absolute;inset:0;width:100%;height:100%}
  .call-bar__label{position:relative;font-family:"Oswald",sans-serif;font-weight:700;font-size:19px;line-height:.95;margin-right:10px}
  .call-bar__icon{position:relative;width:44px;height:44px;margin-right:10px;flex:none}
  .call-bar__number{position:relative;font-family:"Oswald",sans-serif;font-weight:700;font-size:46px;letter-spacing:1px;text-shadow:0 2px 4px var(--shadow)}
  .flyer--front .call-bar{top:668px;width:430px;padding-left:34px}
  .flyer--front .call-bar__number{font-size:40px;letter-spacing:.5px}
  .flyer--back .call-bar{top:668px;width:510px;padding-left:38px}

  .service-list{position:absolute;left:0;right:0;top:146px;list-style:none;text-align:center}
  .service-list li{font-weight:700;font-size:32px;line-height:44.5px;color:var(--gold);text-shadow:0 2px 4px var(--shadow)}
  .service-list .indent{display:block}
  .service-list .bolt{width:20px;height:28px;vertical-align:-3px;margin-right:6px}
</style>
</head>
<body>

<section class="flyer flyer--front" aria-label="Flyer front – discount offer">
  <svg class="decor" viewBox="0 0 540 764" aria-hidden="true">
    <polygon points="0,330 70,330 330,764 240,764" fill="#ffffff" opacity=".9"/>
    <polygon points="0,470 40,470 215,764 150,764" fill="#ffffff" opacity=".85"/>
    <polygon points="70,330 140,330 390,764 330,764" fill="#bfe3ff" opacity=".35"/>
  </svg>

  <div class="fan-photo" role="img" aria-label="Photo of a modern white ceiling fan with LED light"></div>

  <svg class="corner-arrow" viewBox="0 0 130 110" aria-hidden="true">
    <polygon points="0,0 110,0 0,95" fill="#ffffff" opacity=".9"/>
    <polygon points="110,0 130,0 130,30 20,110 0,95" fill="#7fc4f5"/>
    <path d="M18,52 Q40,14 82,26" fill="none" stroke="#ffe100" stroke-width="13" stroke-linecap="round"/>
    <polygon points="78,8 104,34 70,46" fill="#ffe100"/>
  </svg>

  <div class="brand" style="top:48px">
    <span class="brand__name">VoltMate</span>
    <span class="brand__sub">Electrical Services</span>
  </div>

  <p class="tagline">'Keep cool, stay safe and<br>save power with VoltMate'</p>

  <p class="offer-intro">
    <span class="offer-intro__line">During the months of</span>
    <span class="offer-intro__months">October &amp; November</span>
    <span class="offer-intro__line">receive a <span class="offer-intro__pct">10%</span> discount on</span>
  </p>

  <ul class="deal-list">
    <li><svg class="bolt" viewBox="0 0 20 28"><polygon points="13,0 2,16 9,16 6,28 18,10 11,10" fill="#ff8a00" stroke="#fff" stroke-width="1.5"/></svg>Ceiling fan installation</li>
    <li><svg class="bolt" viewBox="0 0 20 28"><polygon points="13,0 2,16 9,16 6,28 18,10 11,10" fill="#ff8a00" stroke="#fff" stroke-width="1.5"/></svg>Smoke alarm installation</li>
    <li><svg class="bolt" viewBox="0 0 20 28"><polygon points="13,0 2,16 9,16 6,28 18,10 11,10" fill="#ff8a00" stroke="#fff" stroke-width="1.5"/></svg>Replace existing downlights for</li>
    <li>new LED downlights</li>
  </ul>

  <p class="expiry">**Offer expires 30th November 2016</p>

  <div class="call-bar">
    <svg class="call-bar__band" viewBox="0 0 430 80" preserveAspectRatio="none" aria-hidden="true">
      <polygon points="14,0 430,0 430,80 0,80" fill="#1b7fd8"/>
      <polygon points="14,0 26,0 12,80 0,80" fill="#7fc4f5"/>
    </svg>
    <span class="call-bar__label">CALL<br>NOW</span>
    <svg class="call-bar__icon" viewBox="0 0 44 44" aria-hidden="true">
      <circle cx="22" cy="22" r="21" fill="#fff"/>
      <path d="M15,12 l5,-1 3,7 -3,2 q2,5 7,7 l2,-3 7,3 -1,5 q-12,1 -18,-12 q-3,-5 -2,-8z" fill="#1b3e8a"/>
    </svg>
    <span class="call-bar__number">XXX-XXX-XXXX</span>
  </div>
</section>

<section class="flyer flyer--back" aria-label="Flyer back – services">
  <svg class="decor" viewBox="0 0 540 764" aria-hidden="true">
    <polygon points="0,140 260,0 540,0 540,60 0,360" fill="#4a6fe0" opacity=".25"/>
  </svg>

  <svg class="corner-arrow" viewBox="0 0 130 110" aria-hidden="true">
    <polygon points="0,0 110,0 0,95" fill="#5aa8f0" opacity=".8"/>
    <polygon points="110,0 130,0 130,30 20,110 0,95" fill="#2d7fe0"/>
    <path d="M18,52 Q40,14 82,26" fill="none" stroke="#ffe100" stroke-width="13" stroke-linecap="round"/>
    <polygon points="78,8 104,34 70,46" fill="#ffe100"/>
  </svg>

  <div class="brand" style="top:46px;right:28px">
    <span class="brand__name">VoltMate</span>
    <span class="brand__sub">Electrical Services</span>
  </div>

  <ul class="service-list">
    <li><svg class="bolt" viewBox="0 0 20 28"><polygon points="13,0 2,16 9,16 6,28 18,10 11,10" fill="#ffd200"/></svg>All residential &amp; commercial<span class="indent">electrical services</span></li>
    <li><svg class="bolt" viewBox="0 0 20 28"><polygon points="13,0 2,16 9,16 6,28 18,10 11,10" fill="#ffd200"/></svg>Electrical contracting</li>
    <li><svg class="bolt" viewBox="0 0 20 28"><polygon points="13,0 2,16 9,16 6,28 18,10 11,10" fill="#ffd200"/></svg>Real estate/strata electrical<span class="indent">maintenance &amp; repairs</span></li>
    <li><svg class="bolt" viewBox="0 0 20 28"><polygon points="13,0 2,16 9,16 6,28 18,10 11,10" fill="#ffd200"/></svg>New builds</li>
    <li><svg class="bolt" viewBox="0 0 20 28"><polygon points="13,0 2,16 9,16 6,28 18,10 11,10" fill="#ffd200"/></svg>Renovations</li>
    <li><svg class="bolt" viewBox="0 0 20 28"><polygon points="13,0 2,16 9,16 6,28 18,10 11,10" fill="#ffd200"/></svg>Security sensor lighting</li>
    <li><svg class="bolt" viewBox="0 0 20 28"><polygon points="13,0 2,16 9,16 6,28 18,10 11,10" fill="#ffd200"/></svg>Ceiling fans</li>
    <li><svg class="bolt" viewBox="0 0 20 28"><polygon points="13,0 2,16 9,16 6,28 18,10 11,10" fill="#ffd200"/></svg>Smoke Alarms</li>
    <li><svg class="bolt" viewBox="0 0 20 28"><polygon points="13,0 2,16 9,16 6,28 18,10 11,10" fill="#ffd200"/></svg>Data connections</li>
  </ul>

  <div class="call-bar">
    <svg class="call-bar__band" viewBox="0 0 510 80" preserveAspectRatio="none" aria-hidden="true">
      <polygon points="14,0 510,0 510,80 0,80" fill="#1b7fd8"/>
      <polygon points="14,0 26,0 12,80 0,80" fill="#7fc4f5"/>
    </svg>
    <span class="call-bar__label">CALL<br>NOW</span>
    <svg class="call-bar__icon" viewBox="0 0 44 44" aria-hidden="true">
      <circle cx="22" cy="22" r="21" fill="#fff"/>
      <path d="M15,12 l5,-1 3,7 -3,2 q2,5 7,7 l2,-3 7,3 -1,5 q-12,1 -18,-12 q-3,-5 -2,-8z" fill="#1b3e8a"/>
    </svg>
    <span class="call-bar__number">XXX-XXX-XXXX</span>
  </div>
</section>

</body>
</html>
```